Would like to reproduce this screen to look more modern

My app is a place for farmers to post jobs a when needing help around the Farm, and local farmhands can apply for the job. The Farmer can then review multiple applicants and select the one best fit for the task at hand. I'm trying to give my screens an updated look while keeping my current color scheme and flow. I would like for you guys to recreate this screen with an updated look the best you can. The main screen with the PX will stay the same. I put that in there to show our logo and our main colors. They look outdated. the other 2 screens are looking at the customers profile, and the screen that u fill out to post a new job.

Target Market(s)

Farmers and farm employees inside the US

Industry/Entity Type

Agriculture

Requirements
Must have
• the same components for the flow but a new look
Nice to have
• ...
Should not have
• Should not change any features, but we can change how buttons look

```html
<!DOCTYPE html>
<html lang="en">
<head>
<meta charset="utf-8">
<title>Farmhand App Screens</title>
<link href="https://fonts.googleapis.com/css2?family=Nunito+Sans:wght@400;600;700;800&display=swap" rel="stylesheet">
<style>
:root{
  --bg-top:#3f7045;
  --bg-bottom:#4a7d3c;
  --brand:#3d6b35;
  --brand-light:#6fbf3f;
  --ink:#1d1d1f;
  --muted:#8e9196;
  --field:#f5f6f8;
  --surface:#ffffff;
  --star:#f5b53a;
}
*{box-sizing:border-box;margin:0;padding:0}
html,body{width:684px;height:1200px;overflow:hidden}
body{
  font-family:"Nunito Sans",Arial,sans-serif;
  background:linear-gradient(180deg,var(--bg-top),var(--bg-bottom));
  position:relative;color:var(--ink);
}
.brand-mark{position:absolute;top:48px;left:299px;width:86px;height:86px;border-radius:50%;background:var(--brand-light)}

.screen{position:absolute;width:375px;background:var(--surface);transform-origin:top left;transform:scale(.84);overflow:hidden}
.screen--profile{left:15px;top:190px;height:812px}
.screen--job{left:354px;top:190px;height:930px}
.abs{position:absolute}

.status-time{left:34px;top:16px;font-size:15px;font-weight:800;line-height:1}
.status-icons{right:16px;top:18px}
.title{left:0;width:375px;text-align:center;font-size:10px;font-weight:800;letter-spacing:1px;line-height:14px}

/* profile */
.profile-head{left:0;top:0;width:375px;height:510px;background:var(--field);border-radius:0 0 32px 32px}
.avatar{left:127px;top:100px;width:120px;height:120px;border-radius:28px;background:linear-gradient(160deg,#a89a86,#6d6558 55%,#3e4f6e)}
.rating{left:162px;top:208px;width:50px;height:22px;border-radius:11px;background:#fff;display:flex;align-items:center;justify-content:center;gap:4px;font-size:11px;color:var(--star)}
.name{left:0;width:375px;top:250px;text-align:center;font-size:16px;font-weight:700;line-height:20px}
.phone{left:0;width:375px;top:274px;text-align:center;font-size:11px;color:var(--muted);line-height:14px}
.detail{left:24px;width:327px;height:20px;display:flex;justify-content:space-between;align-items:center;font-size:14px;font-weight:700;line-height:20px}
.detail .edit{font-size:11px;font-weight:400;color:var(--brand-light)}
.farm-img{top:416px;width:70px;height:70px;border-radius:14px}
.edit-images{left:282px;top:416px;width:70px;height:70px;border:1px dashed #d5d8dc;border-radius:14px;display:flex;align-items:center;justify-content:center;text-align:center;font-size:11px;line-height:1.3;color:var(--brand)}
.section-title{left:24px;top:534px;font-size:16px;font-weight:700;color:var(--brand);line-height:20px}
.job-row{left:24px;width:327px;height:46px;display:flex;align-items:center}
.job-count{width:46px;height:46px;border-radius:50%;background:var(--field);display:flex;align-items:center;justify-content:center;font-size:11px;font-weight:800}
.job-label{flex:1;margin-left:10px;font-size:11px}

/* job form */
.form-head{left:0;top:0;width:375px;height:95px;background:var(--field)}
.label{left:24px;font-size:11px;font-weight:800;line-height:14px}
.field{left:24px;width:327px;height:48px;border-radius:24px;background:var(--field);display:flex;align-items:center;justify-content:space-between;padding:0 20px 0 16px;font-size:11px}
.field--half{width:154px;color:var(--muted)}
.radios{left:24px;top:316px;display:flex;gap:16px;font-size:11px;font-weight:700}
.radio{display:flex;align-items:center;gap:8px}
.radio i{width:20px;height:20px;border-radius:50%;border:1px solid #d5d8dc;display:block}
.radio--on i{border:4px solid #e8ece8;background:var(--brand)}
.create-btn{left:24px;top:858px;width:327px;height:48px;border-radius:24px;background:var(--brand);color:#fff;font-size:14px;font-weight:700;display:flex;align-items:center;justify-content:center}
</style>
</head>
<body>

<div class="brand-mark" role="img" aria-label="App badge"></div>

<svg width="0" height="0" style="position:absolute">
  <symbol id="chev-down" viewBox="0 0 10 6"><path d="M1 1l4 4 4-4" fill="none" stroke="#1d1d1f" stroke-width="1.6" stroke-linecap="round"/></symbol>
  <symbol id="chev-right" viewBox="0 0 6 10"><path d="M1 1l4 4-4 4" fill="none" stroke="#1d1d1f" stroke-width="1.6" stroke-linecap="round"/></symbol>
  <symbol id="status" viewBox="0 0 60 12"><rect x="0" y="8" width="3" height="4" fill="#1d1d1f"/><rect x="4" y="6" width="3" height="6" fill="#1d1d1f"/><rect x="8" y="3" width="3" height="9" fill="#1d1d1f"/><rect x="12" y="0" width="3" height="12" fill="#1d1d1f"/><path d="M21 5a9 9 0 0 1 12 0M23.5 7.5a5 5 0 0 1 7 0" fill="none" stroke="#1d1d1f" stroke-width="1.6"/><circle cx="27" cy="10" r="1.5" fill="#1d1d1f"/><rect x="40" y="2" width="18" height="8" rx="2" fill="#1d1d1f"/></symbol>
</svg>

<!-- Profile screen -->
<section class="screen screen--profile">
  <div class="abs profile-head"></div>
  <div class="abs status-time">4:08</div>
  <svg class="abs status-icons" width="66" height="12"><use href="#status"/></svg>
  <div class="abs title" style="top:60px">MY PROFILE</div>
  <svg class="abs" style="left:343px;top:57px" width="4" height="16"><circle cx="2" cy="2" r="1.6"/><circle cx="2" cy="8" r="1.6"/><circle cx="2" cy="14" r="1.6"/></svg>
  <div class="abs avatar" role="img" aria-label="Profile photo of the farmhand"></div>
  <div class="abs rating"><svg width="12" height="12" viewBox="0 0 24 24"><path d="M12 2l3 7 7 .6-5.4 4.7 1.7 7.2L12 17.7 5.7 21.5l1.7-7.2L2 9.6 9 9z" fill="var(--star)"/></svg>4</div>
  <div class="abs name">Daniel Hartwell</div>
  <div class="abs phone">5550147822</div>
  <div class="abs detail" style="top:306px">User Details<span class="edit">Edit</span></div>
  <div class="abs detail" style="top:340px">Education Details<span class="edit">Edit</span></div>
  <div class="abs detail" style="top:374px">Farm Details<span class="edit">Edit</span></div>
  <div class="abs farm-img" style="left:24px;background:linear-gradient(180deg,#3f4a36,#5f8a3a)" role="img" aria-label="Farm photo: barn and grass field"></div>
  <div class="abs farm-img" style="left:110px;background:linear-gradient(160deg,#d8e6d0,#6a9c45 60%,#e0822c)" role="img" aria-label="Farm photo: orange tree with fruit"></div>
  <div class="abs farm-img" style="left:196px;background:linear-gradient(180deg,#5a8fc8,#9ab5c8 40%,#3d6e2c)" role="img" aria-label="Farm photo: open field with barns"></div>
  <div class="abs edit-images">Edit<br>Images</div>
  <div class="abs section-title">Farmhand Jobs</div>
  <div class="abs job-row" style="top:572px"><span class="job-count">03</span><span class="job-label">Applied jobs</span><svg width="7" height="11"><use href="#chev-right"/></svg></div>
  <div class="abs job-row" style="top:636px"><span class="job-count">00</span><span class="job-label">Scheduled jobs</span><svg width="7" height="11"><use href="#chev-right"/></svg></div>
  <div class="abs job-row" style="top:700px"><span class="job-count">02</span><span class="job-label">Received jobs</span><svg width="7" height="11"><use href="#chev-right"/></svg></div>
  <div class="abs job-row" style="top:764px"><span class="job-count">01</span><span class="job-label">Favorite jobs</span><svg width="7" height="11"><use href="#chev-right"/></svg></div>
</section>

<!-- Create job screen -->
<section class="screen screen--job">
  <div class="abs form-head"></div>
  <div class="abs status-time">4:08</div>
  <svg class="abs status-icons" width="66" height="12"><use href="#status"/></svg>
  <svg class="abs" style="left:31px;top:61px;transform:rotate(180deg)" width="7" height="11"><use href="#chev-right"/></svg>
  <div class="abs title" style="top:60px">CREATE NEW JOB</div>

  <div class="abs label" style="top:120px">Job Category</div>
  <div class="abs field" style="top:144px">Select category<svg width="10" height="6"><use href="#chev-down"/></svg></div>
  <div class="abs label" style="top:216px">Job Title</div>
  <div class="abs field" style="top:240px"></div>

  <div class="abs radios">
    <span class="radio radio--on"><i></i>Hourly Rate</span>
    <span class="radio"><i></i>Fixed Salary</span>
    <span class="radio"><i></i>Per Acre</span>
  </div>

  <div class="abs label" style="top:360px">From</div>
  <div class="abs label" style="top:360px;left:196px">To</div>
  <div class="abs field field--half" style="top:384px">Amount ($)</div>
  <div class="abs field field--half" style="top:384px;left:196px">Amount ($)</div>

  <div class="abs label" style="top:456px">Job Type</div>
  <div class="abs field" style="top:480px">Select job type<svg width="10" height="6"><use href="#chev-down"/></svg></div>
  <div class="abs label" style="top:552px">Equipment Provided</div>
  <div class="abs field" style="top:576px">Select equipment<svg width="10" height="6"><use href="#chev-down"/></svg></div>
  <div class="abs label" style="top:648px">Start Date &amp; Time</div>
  <div class="abs field" style="top:672px">Select start date and time<svg width="10" height="6"><use href="#chev-down"/></svg></div>
  <div class="abs label" style="top:744px">End Date &amp; Time</div>
  <div class="abs field" style="top:768px">Select end date and time<svg width="10" height="6"><use href="#chev-down"/></svg></div>

  <div class="abs create-btn">Create Job</div>
</section>

</body>
</html>
```